Digital menu Skydiving company

Design Digital menu/pricelist for our company. It can have dynamic components. We are also looking for a Graphic design for all our projects. Our main goals are to look clean/sharp and professional. Information is in psd file

3 packages Violet Plunge, Meadow Journey, And Lantern Voyage. then we have addons and merchandise

Colors
0293ce
34a7d8
ffffff
fbee3f
3377b5
000000
f37122
ec1f27
e34197

Requirements
Must have
• Sorry If I couldn't get my vision across better, Please see really rough design idea attached. one large picture section that rotates through 3 or 4 pictures. then all the information down the bottom and on right (see menu pricelist attached)

```html
<!DOCTYPE html>
<html lang="en">
<head>
<meta charset="utf-8">
<title>Altura Skydive – Packages &amp; Pricing</title>
<link href="https://fonts.googleapis.com/css2?family=Montserrat:wght@500;700;800;900&display=swap" rel="stylesheet">
<style>
  :root {
    --white: #ffffff;
    --ink: #1a1d22;
    --navy: #0d3f7a;
    --banner-dark: #0b2f6b;
    --banner-light: #1f78b8;
    --label-top: #0f4f66;
    --label-bottom: #16181c;
    --desc-left: #1266a8;
    --desc-right: #0378c9;
    --price-top: #173f78;
    --price-bottom: #0a5a7c;
    --extra-left: #0f6db6;
    --extra-right: #0890e0;
    --sky: #0293ce;
    --screen-top: #f4f6f9;
    --screen-bottom: #dff1fb;
  }
  * { margin: 0; padding: 0; box-sizing: border-box; }
  html, body { width: 1200px; height: 811px; overflow: hidden; }
  body {
    font-family: "Montserrat", sans-serif;
    background: linear-gradient(180deg, var(--screen-top) 0%, #eef3f8 60%, var(--screen-bottom) 100%);
    position: relative;
    color: var(--white);
  }
  .header-banner { position: absolute; left: 0; top: 0; width: 1200px; height: 160px; }
  .brand {
    position: absolute; left: 28px; top: 52px;
    display: flex; align-items: center; gap: 10px;
    font-weight: 800; font-size: 27px; letter-spacing: 1px;
    color: var(--ink); text-transform: uppercase;
  }
  .brand-dot { width: 18px; height: 18px; border-radius: 50%; background: var(--sky); }
  .page-title {
    position: absolute; right: 29px; top: 38px;
    font-weight: 900; font-size: 63px; letter-spacing: 0.5px; line-height: 1;
  }
  .package {
    position: absolute; left: 0; width: 1189px; height: 184px;
    display: grid; grid-template-columns: 189px 393px 315px 292px;
  }
  .package-1 { top: 165px; }
  .package-2 { top: 378px; }
  .package-3 { top: 592px; }
  .package-name {
    background: linear-gradient(180deg, var(--label-top), var(--label-bottom));
    display: flex; flex-direction: column; justify-content: center; align-items: flex-end;
    padding-right: 18px; text-align: right;
    font-weight: 800; font-size: 22px; line-height: 1.6; text-transform: uppercase;
  }
  .package-info {
    background: linear-gradient(90deg, var(--desc-left), var(--desc-right));
    padding: 24px 14px 0 26px;
  }
  .tagline { font-weight: 500; font-size: 16px; letter-spacing: 0.4px; margin-bottom: 8px; }
  .includes { list-style: none; }
  .includes li {
    position: relative; font-weight: 800; font-size: 19.5px; line-height: 1.25;
    margin-bottom: 11px; text-transform: uppercase;
  }
  .includes li::before {
    content: ""; position: absolute; left: -16px; top: 5px;
    border-left: 7px solid var(--white); border-top: 6px solid transparent; border-bottom: 6px solid transparent;
  }
  .photo-slot {
    position: relative;
    background: linear-gradient(180deg, #7a86d6 0%, #a69ccf 45%, #c9a3b8 70%, #b79a6a 100%);
  }
  .photo-caption {
    position: absolute; left: 0; right: 0; bottom: 0; height: 38px;
    background: linear-gradient(90deg, rgba(60,60,40,0.55), rgba(90,80,60,0.35));
    display: flex; align-items: center; padding-left: 26px;
    font-weight: 500; font-size: 16px; letter-spacing: 0.4px;
  }
  .price {
    background: linear-gradient(180deg, var(--price-top), var(--price-bottom));
    display: flex; align-items: center; justify-content: center;
    font-weight: 900; font-size: 98px; letter-spacing: -2px; line-height: 1;
    color: #f2f2f2; text-shadow: 2px 2px 0 rgba(0,0,0,0.15);
  }
  .extras {
    background: linear-gradient(90deg, var(--extra-left), var(--extra-right));
    padding: 28px 16px 0 10px; list-style: none;
  }
  .extras li {
    display: flex; justify-content: space-between; align-items: flex-start;
    font-weight: 700; font-size: 13.5px; line-height: 1.25; margin-bottom: 8.5px;
    text-transform: uppercase;
  }
  .extras li .item { position: relative; padding-left: 12px; }
  .extras li .item::before { content: "•"; position: absolute; left: 0; top: 0; }
  .extras li .cost { font-size: 14.5px; }
  .extras.plain { padding-top: 26px; }
</style>
</head>
<body>
  <svg class="header-banner" viewBox="0 0 1200 160" aria-hidden="true">
    <defs>
      <linearGradient id="bannerFill" x1="0" y1="0" x2="0" y2="1">
        <stop offset="0" stop-color="#2a6fae"/>
        <stop offset="0.35" stop-color="#0b2f6b"/>
        <stop offset="1" stop-color="#1b7db8"/>
      </linearGradient>
    </defs>
    <polygon points="0,0 1200,0 1200,160 0,160" fill="#ffffff"/>
    <polygon points="319,12 1200,12 1200,139 247,139" fill="url(#bannerFill)"/>
    <polygon points="247,139 1200,139 1200,146 243,146" fill="#e9eef4"/>
  </svg>

  <div class="brand"><span class="brand-dot"></span>Altura Skydive</div>
  <h1 class="page-title">PACKAGES &amp; PRICING</h1>

  <section class="package package-1">
    <h2 class="package-name"><span>Violet</span><span>Plunge</span><span>16,000FT</span></h2>
    <div class="package-info">
      <p class="tagline">THE SKYDIVE IS NAKED, NOT YOU...</p>
      <ul class="includes">
        <li>Certificate of Achievement</li>
        <li>Tandem Skydive from<br>16,000FT MSL</li>
      </ul>
    </div>
    <div class="price">$329</div>
    <ul class="extras">
      <li><span class="item">T-Shirt Short Sleeve</span><span class="cost">$20</span></li>
      <li><span class="item">T-Shirt Long Sleeve</span><span class="cost">$28</span></li>
      <li><span class="item">Sweat Shirts</span><span class="cost">$30</span></li>
      <li><span class="item">Hoodies</span><span class="cost">$38</span></li>
      <li><span class="item">Goggles From</span><span class="cost">$12</span></li>
    </ul>
  </section>

  <section class="package package-2">
    <h2 class="package-name"><span>Meadow</span><span>Journey</span><span>16,000FT</span></h2>
    <div class="photo-slot" role="img" aria-label="Photo of a tandem skydiving pair in free fall against a violet evening sky">
      <p class="photo-caption">SKYDIVE &amp; SHARE THE MEMORIES...</p>
    </div>
    <div class="price">$459</div>
    <ul class="extras plain">
      <li><span class="item">Tandem Skydive from<br>16,000FT MSL</span></li>
      <li><span class="item">Photos</span></li>
      <li><span class="item">Videos</span></li>
      <li><span class="item">Certificate of Achievement</span></li>
    </ul>
  </section>

  <section class="package package-3">
    <h2 class="package-name"><span>Lantern</span><span>Voyage</span><span>16,000FT</span></h2>
    <div class="package-info">
      <p class="tagline">FOR THE THRILL SEEKER...</p>
      <ul class="includes">
        <li>Altura Skydive</li>
        <li>Certificate of Achievement</li>
      </ul>
    </div>
    <div class="price">$499</div>
    <ul class="extras plain">
      <li><span class="item">Tandem Skydive from<br>16,000FT MSL</span><span class="cost">$319</span></li>
      <li><span class="item">Photos</span><span class="cost">$99</span></li>
      <li><span class="item">Videos</span><span class="cost">$99</span></li>
      <li><span class="item">Extreme Extras</span><span class="cost">$50</span></li>
    </ul>
  </section>
</body>
</html>
```